Stationary For Engineering & Consultancy Company
Harbourline Sound Consulting Inc.
Stationary For Engineering & Consultancy Company - Consulting
Professional
Rajveer Talwani
President (MSc. Applied tremolo)
42 Willowmere Crt, Brampton, Ontario L6R 3J8
info@harbourlinesound.example
www.harbourlinesound.example

```html
<!DOCTYPE html>
<html lang="en">
<head>
<meta charset="utf-8">
<title>Harbourline Sound Consulting Inc. – Business Card</title>
<link rel="stylesheet" href="https://fonts.googleapis.com/css2?family=Open+Sans:wght@400;600;700&display=swap">
<style>
  :root {
    --backdrop: #d9d9d9;
    --card: #ffffff;
    --ink: #3a3a3a;
    --ink-soft: #6b6b6b;
    --green-dark: #2f5a12;
    --green: #4f8a1c;
    --green-light: #8cc63f;
    --pill: #3b3b3b;
    --white: #ffffff;
  }
  * { box-sizing: border-box; margin: 0; padding: 0; }
  html, body { width: 1200px; height: 895px; overflow: hidden; }
  body {
    background: var(--backdrop);
    font-family: "Open Sans", Arial, sans-serif;
    color: var(--ink);
    display: flex;
    align-items: center;
    justify-content: center;
    gap: 40px;
  }
  .card {
    position: relative;
    width: 560px;
    height: 320px;
    background: var(--card);
    overflow: hidden;
    box-shadow: 0 2px 6px rgba(0,0,0,.12);
  }
  .brand {
    display: flex;
    align-items: center;
    gap: 10px;
  }
  .brand-mark {
    width: 34px;
    height: 34px;
    background: var(--green);
    flex: none;
  }
  .brand-name {
    font-weight: 600;
    color: var(--green);
    font-size: 17px;
    line-height: 1.15;
    letter-spacing: .3px;
  }
  .brand-tagline {
    font-size: 8px;
    color: var(--ink-soft);
    letter-spacing: 1px;
    text-transform: uppercase;
    margin-top: 3px;
  }

  /* Front */
  .card-front .brand { position: absolute; left: 36px; top: 38px; }
  .holder {
    position: absolute;
    left: 36px;
    top: 140px;
  }
  .holder-line { display: flex; align-items: baseline; gap: 10px; }
  .holder-name { font-size: 22px; font-weight: 700; color: var(--ink); }
  .holder-role { font-size: 15px; color: var(--ink); border-left: 2px solid var(--ink); padding-left: 10px; }
  .holder-address { font-size: 12px; font-weight: 600; margin-top: 6px; color: var(--ink); }
  .contact-band {
    position: absolute;
    left: 0;
    top: 222px;
    width: 500px;
    height: 34px;
    border-radius: 0 17px 17px 0;
    background: linear-gradient(90deg, var(--green-dark), var(--green) 55%, var(--green-light));
    display: flex;
    align-items: center;
    gap: 22px;
    padding-left: 30px;
    color: var(--white);
    font-size: 12px;
  }
  .contact-item { display: flex; align-items: center; gap: 6px; white-space: nowrap; }
  .contact-icon { width: 16px; height: 16px; flex: none; }

  /* Back */
  .card-back .brand { position: absolute; left: 170px; top: 100px; }
  .card-back .brand-mark { width: 42px; height: 42px; }
  .card-back .brand-name { font-size: 20px; }
  .web-pill {
    position: absolute;
    left: 0;
    top: 210px;
    width: 300px;
    height: 30px;
    background: var(--pill);
    border-radius: 0 15px 15px 0;
    color: var(--white);
    font-size: 13px;
    display: flex;
    align-items: center;
    padding-left: 30px;
    letter-spacing: .3px;
  }
</style>
</head>
<body>

<section class="card card-front" aria-label="Business card front">
  <div class="brand">
    <span class="brand-mark"></span>
    <div>
      <div class="brand-name">Harbourline Sound<br>Consulting Inc.</div>
      <div class="brand-tagline">Sound Engineering Consultants</div>
    </div>
  </div>

  <div class="holder">
    <div class="holder-line">
      <span class="holder-name">Rajveer Talwani</span>
      <span class="holder-role">President &amp; Ceo</span>
    </div>
    <div class="holder-address">42 Willowmere Crt, Brampton, Ontario L6R 3J8</div>
  </div>

  <div class="contact-band">
    <span class="contact-item">
      <svg class="contact-icon" viewBox="0 0 16 16" aria-hidden="true"><circle cx="8" cy="8" r="8" fill="#fff"/><path d="M5.2 4.2l1.4-.2.7 1.8-.9.7a5 5 0 0 0 2.3 2.3l.7-.9 1.8.7-.2 1.4c-3.2.3-6.1-2.6-5.8-5.8z" fill="#2f5a12"/></svg>
      555 014 2290
    </span>
    <span class="contact-item">
      <svg class="contact-icon" viewBox="0 0 16 16" aria-hidden="true"><circle cx="8" cy="8" r="8" fill="#fff"/><path d="M5.2 4.2l1.4-.2.7 1.8-.9.7a5 5 0 0 0 2.3 2.3l.7-.9 1.8.7-.2 1.4c-3.2.3-6.1-2.6-5.8-5.8z" fill="#4f8a1c"/></svg>
      555 014 2291
    </span>
    <span class="contact-item">
      <svg class="contact-icon" viewBox="0 0 16 16" aria-hidden="true"><circle cx="8" cy="8" r="8" fill="#fff"/><rect x="4" y="5.2" width="8" height="5.6" fill="none" stroke="#6aa52a" stroke-width="1"/><path d="M4 5.4l4 3 4-3" fill="none" stroke="#6aa52a" stroke-width="1"/></svg>
      info@harbourlinesound.example
    </span>
  </div>
</section>

<section class="card card-back" aria-label="Business card back">
  <div class="brand">
    <span class="brand-mark"></span>
    <div>
      <div class="brand-name">Harbourline Sound<br>Consulting Inc.</div>
      <div class="brand-tagline">Sound Engineering Consultants</div>
    </div>
  </div>
  <div class="web-pill">www.harbourlinesound.example</div>
</section>

</body>
</html>
```